Zelvo - revolutionary mobile payment

The app is a P2P money trasfert, without the using of credit card or bank circuits it can transfer electronic money from one person to another consumers simply and immediatelly.
You can use the color you want, but the message we need to transert to consumer is simplicity, safety and coolness.
In attach the logo of the company and the wireframe of thre page of the app.
The goal is to design the page of the app with a clear, simple and intuitive graphic.
Updates

I have upgrade the brief with important information and detail, many thanks

Target Market(s)

all the people

Industry/Entity Type

Credit Card

Requirements
Must have
• You have to design one icon for each button in the first page, (shop is: where to shop)
in the second one a new intuitive image (instead of the hand) that let the user to understand that with a simple swipe he can process the payment
Nice to have
• You can include or esxclude what you want or belive can improve user experience of the app
Should not have
• too much color, too much button or information

```html
<!DOCTYPE html>
<html lang="en">
<head>
<meta charset="UTF-8">
<title>Zelvo – mobile payment home screen</title>
<link rel="stylesheet" href="https://fonts.googleapis.com/css2?family=Open+Sans:wght@400;600;700&family=Raleway:wght@300&display=swap">
<style>
  :root {
    --navy: #1c3160;
    --ink: #3a4a6a;
    --page-bg: #f4f3e6;
    --screen-bg: #f7f7f7;
    --tile-bg: #f4f4f4;
    --tile-border: #dadada;
    --white: #ffffff;
    --avatar-tone: linear-gradient(160deg, #c9cfd6 0%, #8a7a6e 55%, #2b2e36 100%);
  }
  * { box-sizing: border-box; margin: 0; padding: 0; }
  html, body { width: 960px; height: 1200px; overflow: hidden; }
  body {
    background: var(--page-bg);
    font-family: "Open Sans", sans-serif;
    position: relative;
  }

  .brand {
    position: absolute; left: 52px; top: 40px;
    display: flex; align-items: center; gap: 14px;
  }
  .brand-dot {
    width: 74px; height: 74px; border-radius: 50%;
    border: 9px solid var(--navy);
  }
  .brand-name {
    font-family: "Open Sans", sans-serif;
    font-weight: 700; font-size: 58px; color: var(--navy);
    letter-spacing: 1px;
  }
  .intro {
    position: absolute; left: 60px; top: 144px; width: 440px;
    font-family: "Raleway", sans-serif; font-weight: 300;
    font-size: 15.5px; line-height: 21px; color: var(--ink);
  }

  .app-screen {
    position: absolute; left: 304px; top: 396px;
    width: 328px; height: 582px;
    background: var(--screen-bg);
    overflow: hidden;
    box-shadow: 0 10px 30px rgba(28, 49, 96, 0.15);
  }
  .top-bar {
    height: 37px; background: var(--navy);
    display: flex; align-items: center; padding: 0 10px;
    color: var(--white);
  }
  .top-bar .back { width: 14px; height: 14px; margin-right: 14px; }
  .top-bar .bar-brand {
    font-weight: 700; font-size: 15px; flex: 1; letter-spacing: .5px;
  }
  .top-bar .menu { width: 16px; height: 14px; }

  .profile {
    background: var(--white); height: 161px;
    display: flex; flex-direction: column; align-items: center;
    padding-top: 27px;
  }
  .avatar {
    width: 94px; height: 94px; border-radius: 50%;
    background: var(--avatar-tone);
  }
  .profile-name {
    margin-top: 14px; font-size: 15px; color: var(--navy);
  }

  .action-grid {
    position: absolute; left: 12px; top: 222px;
    display: grid; grid-template-columns: 149px 149px;
    grid-auto-rows: 146px; gap: 8px;
  }
  .action-tile {
    background: var(--tile-bg); border: 1px solid var(--tile-border);
    display: flex; flex-direction: column; align-items: center;
    justify-content: center; gap: 10px;
    color: var(--navy); font-size: 18px;
  }
  .action-tile svg { width: 56px; height: 56px; }
</style>
</head>
<body>

  <header class="brand">
    <span class="brand-dot"></span>
    <span class="brand-name">Zelvo</span>
  </header>
  <p class="intro">The app is a P2P money trasfert, without the using of credit card or bank circuits it can transfer electronic money from one person to another consumers simply and immediatelly.</p>

  <main class="app-screen">
    <nav class="top-bar">
      <svg class="back" viewBox="0 0 14 14"><path d="M9 2 L4 7 L9 12" fill="none" stroke="#fff" stroke-width="1.6"/></svg>
      <span class="bar-brand">Zelvo</span>
      <svg class="menu" viewBox="0 0 16 14"><path d="M0 2h16M0 7h16M0 12h16" stroke="#fff" stroke-width="2"/></svg>
    </nav>

    <section class="profile">
      <div class="avatar" role="img" aria-label="Profile photo of the account holder"></div>
      <p class="profile-name">Martin Hale</p>
    </section>

    <section class="action-grid">
      <div class="action-tile">
        <svg viewBox="0 0 56 56">
          <rect x="14" y="6" width="26" height="18" rx="2" transform="rotate(-30 27 15)" fill="#1c3160"/>
          <circle cx="27" cy="15" r="5" fill="none" stroke="#fff" stroke-width="1.6"/>
          <path d="M14 30 h18 l8 -6 l4 4 l-8 10 h-22 z" fill="none" stroke="#1c3160" stroke-width="2.4" stroke-linejoin="round"/>
          <rect x="12" y="42" width="12" height="5" fill="#1c3160"/>
        </svg>
        <span>Pay</span>
      </div>
      <div class="action-tile">
        <svg viewBox="0 0 56 56">
          <path d="M28 4 C36 8 44 9 50 9 C50 30 42 44 28 52 C14 44 6 30 6 9 C12 9 20 8 28 4 Z" fill="#1c3160"/>
          <text x="28" y="37" text-anchor="middle" font-family="Open Sans, sans-serif" font-weight="700" font-size="26" fill="#fff">?</text>
        </svg>
        <span>Ask</span>
      </div>
      <div class="action-tile">
        <svg viewBox="0 0 56 56">
          <path d="M18 4 L28 10 L38 4 L34 16 H22 Z" fill="#1c3160"/>
          <path d="M22 18 H34 C46 26 50 40 46 48 C44 52 40 52 28 52 C16 52 12 52 10 48 C6 40 10 26 22 18 Z" fill="#1c3160"/>
          <text x="28" y="44" text-anchor="middle" font-family="Open Sans, sans-serif" font-weight="700" font-size="20" fill="#fff">$</text>
        </svg>
        <span>Account</span>
      </div>
      <div class="action-tile">
        <svg viewBox="0 0 56 56">
          <path d="M3 20 L17 16 L29 20 L42 16 L53 20 V52 L42 48 L29 52 L17 48 L3 52 Z" fill="none" stroke="#1c3160" stroke-width="2.2" stroke-linejoin="round"/>
          <path d="M17 16 V48 M29 20 V52 M42 16 V48 M3 36 H53" stroke="#1c3160" stroke-width="2"/>
          <path d="M24 4 a9 9 0 0 1 9 9 c0 7 -9 16 -9 16 s-9 -9 -9 -16 a9 9 0 0 1 9 -9 z" fill="#1c3160"/>
          <circle cx="24" cy="13" r="3.4" fill="#fff"/>
        </svg>
        <span>Shop</span>
      </div>
    </section>
  </main>

</body>
</html>
```